Infographic for open source project (over-the-air updates for connected devices)

We would like an infographic created. It can be 1-2 pages. Our project is targeted toward the Internet of Things (connected devices), as it provides a secure and robust way to deploy over-the-air (OTA) software updates for connected Linux devices. This has been broken into 4 broad categories with specific requirements within each.

Please see some content on our website to better understand our design preference:

https://quillarbo.io/resources/customer-case-studies
Updates

Target Market(s)

Embedded system developers, owners of connected device projects (e.g. developers of home automation, industrial automation, smart energy, smart appliances,

Industry/Entity Type

Internet

Requirements
Must have
• Must include all the content included in the xls file attached. Design should follow our StyleGuide (also attached) and the general design aesthetic (e.g. our customer case studies), but creativity is encouraged for the infographic to best present the information in the xls file.

```html
<!DOCTYPE html>
<html lang="en">
<head>
<meta charset="utf-8">
<title>Quillarbo – OTA Update Requirements Infographic</title>
<link href="https://fonts.googleapis.com/css2?family=Exo+2:wght@600;700&family=Open+Sans:wght@400;600&display=swap" rel="stylesheet">
<style>
:root{
  --teal:#135c6b;
  --teal-text:#17707f;
  --plum:#6e2b5c;
  --ink:#3c3c3c;
  --body:#555a5e;
  --rule:#7b3a68;
  --paper:#ffffff;
  --backdrop:#e4e5e7;
}
*{box-sizing:border-box;margin:0;padding:0}
html,body{width:1200px;height:782px;overflow:hidden;background:var(--backdrop)}
body{font-family:"Open Sans",Arial,sans-serif;color:var(--body);position:relative}
.page{position:absolute;top:14px;width:570px;height:754px;background:var(--paper);padding:14px 14px 10px;display:flex;flex-direction:column;overflow:hidden;box-shadow:0 2px 8px rgba(0,0,0,.18)}
.page--left{left:20px}
.page--right{left:610px}
.brand{display:flex;align-items:center;justify-content:center;gap:10px;height:52px;margin-bottom:6px}
.brand__dot{width:30px;height:30px;border-radius:50%;background:var(--plum)}
.brand__name{font-family:"Exo 2",Arial,sans-serif;font-weight:700;font-size:26px;letter-spacing:2px;color:var(--ink)}
.band{background:var(--teal);color:#fff;font-family:"Exo 2",Arial,sans-serif;font-weight:700;font-size:15px;letter-spacing:2.5px;text-align:center;height:20px;line-height:20px;margin:0 -2px}
.table{border:1px solid var(--rule);border-top:none;margin:0 6px 6px}
.head,.row{display:grid;grid-template-columns:29% 29% 42%}
.head{margin:6px -6px 0;border-bottom:1px solid var(--rule)}
.head__cell{display:flex;align-items:center;position:relative;height:26px;padding:0 3px 0 4px;min-width:0}
.head__icon{width:24px;height:24px;flex:none;position:relative;z-index:1}
.head__label{flex:1;min-width:0;margin-left:-8px;height:20px;border:1px solid var(--rule);border-radius:0 6px 6px 0;padding-left:11px;font-family:"Exo 2",Arial,sans-serif;font-weight:700;font-size:11px;line-height:18px;color:var(--teal-text);letter-spacing:.2px;white-space:nowrap;overflow:hidden}
.row{border-bottom:1px solid var(--rule);font-size:6.2px;line-height:1.42}
.row:last-child{border-bottom:none}
.row>p{padding:4px 6px 5px;text-align:justify}
.row>p+p{border-left:1px solid var(--rule)}
.row>.req{text-align:left}
.closing{margin-top:auto;text-align:center;padding-bottom:10px}
.closing__title{font-family:"Exo 2",Arial,sans-serif;font-weight:600;font-size:17px;line-height:1.25;color:var(--teal-text);letter-spacing:.3px}
.closing__tag{font-size:9.5px;margin-top:6px;color:var(--ink)}
</style>
</head>
<body>

<svg width="0" height="0" style="position:absolute" aria-hidden="true">
  <defs>
    <symbol id="ico-req" viewBox="0 0 24 24"><circle cx="12" cy="12" r="11" fill="#fff" stroke="#4a4a4a" stroke-width="1.6"/><rect x="8" y="6.5" width="8" height="11" rx="1" fill="none" stroke="#4a4a4a" stroke-width="1.3"/><path d="M10 9.5h4M10 12h4M10 14.5h3" stroke="#4a4a4a" stroke-width="1"/></symbol>
    <symbol id="ico-desc" viewBox="0 0 24 24"><circle cx="12" cy="12" r="11" fill="#fff" stroke="#4a4a4a" stroke-width="1.6"/><path d="M9 15.5l5.5-5.5a1.6 1.6 0 0 0-2.3-2.3L6.9 13a2.8 2.8 0 0 0 4 4l5.8-5.8" fill="none" stroke="#4a4a4a" stroke-width="1.3" stroke-linecap="round"/></symbol>
    <symbol id="ico-risk" viewBox="0 0 24 24"><circle cx="12" cy="12" r="11" fill="#fff" stroke="#4a4a4a" stroke-width="1.6"/><path d="M12 6.5l6 10.5H6z" fill="none" stroke="#4a4a4a" stroke-width="1.4" stroke-linejoin="round"/><path d="M12 10v3.5" stroke="#4a4a4a" stroke-width="1.4"/><circle cx="12" cy="15.2" r=".8" fill="#4a4a4a"/></symbol>
  </defs>
</svg>

<section class="page page--left">
  <header class="brand"><span class="brand__dot"></span><span class="brand__name">QUILLARBO</span></header>

  <h2 class="band">ROBUST</h2>
  <div class="table">
    <div class="head">
      <div class="head__cell"><svg class="head__icon"><use href="#ico-req"/></svg><span class="head__label">REQUIREMENT</span></div>
      <div class="head__cell"><svg class="head__icon"><use href="#ico-desc"/></svg><span class="head__label">DESCRIPTION</span></div>
      <div class="head__cell"><svg class="head__icon"><use href="#ico-risk"/></svg><span class="head__label">RISKS WHEN NOT IMPLEMENTED</span></div>
    </div>
    <div class="row">
      <p class="req">Update mechanism is immune to power and network loss mid-update in order to avoid any bricked devices</p>
      <p>Atomic installs (full image over package based) where an update is always fully installed or not at all avoids the possibility of a device becoming unbootable due to interruptions of an update. No software component ever sees a partially installed update.</p>
      <p>Devices may be bricked when an update is interrupted due to poor network connectivity or power loss and may become unusable. Non-atomic updates also run the risk of inconsistency across a fleet of devices and becomes unmanageable when production does not match test environments.</p>
    </div>
    <div class="row">
      <p class="req">Rollback to previous working version is built-in and automatic with sanity checks post-installation</p>
      <p>Dual A/B partition is one of the most reliable and simple approaches for built-in rollback where the update is written to the inactive root filesystem partition and the bootloader is configured to boot from it and then the embedded system reboots. Once the updater comes up it will try to report the success of the deployment to the management server. If this fails it will automatically rollback.</p>
      <p>If an update fails for any reason with no ability to rollback to the last working version, sending a technician to the field where the device resides will be costly.</p>
    </div>
    <div class="row">
      <p class="req">Integrity check to avoid corruption</p>
      <p>Make sure the update artifact is not corrupted, end-to-end from build system to device, due to any transfer or hardware issues.</p>
      <p>Intermittent application malfunction, application not starting or device bricking due to random modifications of the update.</p>
    </div>
    <div class="row">
      <p class="req">Compatibility check</p>
      <p>Verifies that the software update can run on the target devices. For example, the CPU architecture of the devices are supported by the software update.</p>
      <p>Application fails to start or the device gets bricked immediately because the software is built for the wrong device type. This is in particular an issue when multiple revisions of devices and software are introduced, and software updates only support a subset of the devices.</p>
    </div>
    <div class="row">
      <p class="req">Ensure another update can be deployed</p>
      <p>After an update has been deployed, make sure that another update can be deployed by making sure that the deployment server can be reached after the update. Otherwise a rollback should be performed.</p>
      <p>If an update makes a device malfunction in certain ways such as losing network connectivity, the device can never be fixed and is effectively bricked.</p>
    </div>
    <div class="row">
      <p class="req">Custom sanity checks after the update</p>
      <p>Even though a device boots, it does not mean that its application works properly. For example, the UI framework may not be brought up. Custom sanity checks are automatically run after the update and the updater automatically rolls back the update if they do not all pass.</p>
      <p>The device may be unusable to the end user because important applications are not brought up after the update or key services are malfunctioning.</p>
    </div>
    <div class="row">
      <p class="req">Well maintained code and high code quality</p>
      <p>The updater is a critical component to an embedded system and needs to be well tested and widely used across a wide variety of use cases so the code maintains a high quality level.</p>
      <p>Bugs in the updater itself can not only brick devices but also expose serious security vulnerabilities to the devices.</p>
    </div>
  </div>

  <h2 class="band">SECURITY</h2>
  <div class="table">
    <div class="head">
      <div class="head__cell"><svg class="head__icon"><use href="#ico-req"/></svg><span class="head__label">REQUIREMENT</span></div>
      <div class="head__cell"><svg class="head__icon"><use href="#ico-desc"/></svg><span class="head__label">DESCRIPTION</span></div>
      <div class="head__cell"><svg class="head__icon"><use href="#ico-risk"/></svg><span class="head__label">RISKS WHEN NOT IMPLEMENTED</span></div>
    </div>
    <div class="row">
      <p class="req">Secure communications between the management server and the client running on the device</p>
      <p>Use of secure and bi-directionally authenticated communication between the client/server (e.g. TLS)</p>
      <p>The update can be modified while in transit from the update server to the device, enabling an attacker to inject malicious code, steal data and take over the device. This attack is particularly susceptible over wireless networks. The attacker could also imitate the update server, forcing a malicious update to be installed at their choosing.</p>
    </div>
    <div class="row">
      <p class="req">Authenticity of update images with code signing</p>
      <p>End-to-end signature management to authenticate it is an authorized and trusted update</p>
      <p>Lack of digital signatures/code signing allows attackers to reprogram sensitive components of the embedded system by modifying a valid update, enabling attackers to inject malicious code or take over the device.</p>
    </div>
  </div>
</section>

<section class="page page--right">
  <header class="brand"><span class="brand__dot"></span><span class="brand__name">QUILLARBO</span></header>

  <h2 class="band">INTEGRATION INTO EXISTING ENVIRONMENTS</h2>
  <div class="table">
    <div class="head">
      <div class="head__cell"><svg class="head__icon"><use href="#ico-req"/></svg><span class="head__label">REQUIREMENT</span></div>
      <div class="head__cell"><svg class="head__icon"><use href="#ico-desc"/></svg><span class="head__label">DESCRIPTION</span></div>
      <div class="head__cell"><svg class="head__icon"><use href="#ico-risk"/></svg><span class="head__label">RISKS WHEN NOT IMPLEMENTED</span></div>
    </div>
    <div class="row">
      <p class="req">Existing development build system integration</p>
      <p>The update process should integrate with existing OSes, development tools and popular build systems like the Kestrel Project.</p>
      <p>Pushback from the development team if the updater dictates the tools they need to use, for example a "rip and replace" solution that dictates the embedded OS, language or how updates are packaged.</p>
    </div>
    <div class="row">
      <p class="req">Standalone deployments</p>
      <p>While OTA is the desired mechanism, many devices will initially require standalone deployments with an update via a USB or SD Card</p>
      <p>If devices without wireless network connectivity cannot be updated, they have an increased security risk and will almost certainly be vulnerable to attacks of publicly known vulnerabilities over time.</p>
    </div>
    <div class="row">
      <p class="req">Support for multiple storage types</p>
      <p>Embedded systems can use a variety of storage, including raw NAND flash, eMMC and SPI-NOR. Besides supporting all these, the updater must not make unnecessary writes to the storage because this will quickly wear out the flash.</p>
      <p>If the updater does not support all embedded storage types used, some devices may never be able to update and thus leave a security issue as software vulnerabilities become public over time. If the updater does not take into account the limited wear requirement of flash-based devices, the devices will get bricked over time.</p>
    </div>
  </div>

  <h2 class="band">FLEET MANAGEMENT</h2>
  <div class="table">
    <div class="head">
      <div class="head__cell"><svg class="head__icon"><use href="#ico-req"/></svg><span class="head__label">REQUIREMENT</span></div>
      <div class="head__cell"><svg class="head__icon"><use href="#ico-desc"/></svg><span class="head__label">DESCRIPTION</span></div>
      <div class="head__cell"><svg class="head__icon"><use href="#ico-risk"/></svg><span class="head__label">RISKS WHEN NOT IMPLEMENTED</span></div>
    </div>
    <div class="row">
      <p class="req">Deployment management server</p>
      <p>Ability to automate deployment across a fleet of devices</p>
      <p>If devices need to be updated one-by-one, deploying updates will be extremely costly or not carried out at all.</p>
    </div>
    <div class="row">
      <p class="req">Rollout management</p>
      <p>The ability to perform phased rollouts and deployments specific to certain groups or locations of the device population</p>
      <p>Updating fleets without rollout management and device groupings will require more man hours to update entire device fleets. When manual tasks are increased, mistakes increase accordingly. If you can only update to all devices, the risk is high that one mistake can brick the entire fleet.</p>
    </div>
    <div class="row">
      <p class="req">Device Inventory</p>
      <p>Ability to list all devices, through an UI and REST API, together with key inventory information such as network addresses, product revision and model and when it last connected to the server infrastructure.</p>
      <p>Lack of device inventory can easily lead to security breaches as "forgotten" devices are no longer maintained.</p>
    </div>
    <div class="row">
      <p class="req">Installed software versions</p>
      <p>Ability to see the current software versions installed on each device and query this information.</p>
      <p>In order to plan for software updates, you need to know what is out there already. This will make it possible to know if the installed software is compatible with the desired update. It is also critical to know which software is installed on all the devices in order to discover which devices are vulnerable to known vulnerabilities and CVEs so that they can be updated.</p>
    </div>
    <div class="row">
      <p class="req">Deployment logs</p>
      <p>Diagnostics logs from devices that are captured as a deployment is carried out</p>
      <p>If a deployment fails across one or more devices and there are no logs, issues are very hard to diagnose and fix.</p>
    </div>
    <div class="row">
      <p class="req">Deployment status reports</p>
      <p>An overall status of the deployment, such as how many devices succeeded and failed the deployment, as well as which devices failed.</p>
      <p>If it is not possible to know if a deployment succeeds or fails and on which devices, deploying updates is very risky as bricking devices can go unnoticed for a very long time. The only way to see failures in this case is when end users report them which leads to a very bad customer experience and an expensive support burden.</p>
    </div>
  </div>

  <footer class="closing">
    <h3 class="closing__title">OVER-THE-AIR SOFTWARE UPDATES FOR<br>EMBEDDED LINUX DEVICES</h3>
    <p class="closing__tag">Quillarbo is an open source tool for updating your embedded devices safely and reliably</p>
  </footer>
</section>

</body>
</html>
```